I have an animal hospital. I want a poster to hang in each exam room to show a picture of a normal sized heart and then an enlarged heart of a dog that was fed a grain-free diet. I want to warn people not to feed grain-free diets. Maybe at the top of the poster, "Do you feed grain-free?" and then the x-ray comparison, then the warnings of Canine Dilated Cardiomyopathy.

```html
<!DOCTYPE html>
<html lang="en">
<head>
<meta charset="utf-8">
<title>Do you feed grain-free? – Exam Room Poster</title>
<link href="https://fonts.googleapis.com/css2?family=Outfit:wght@600;700;800;900&display=swap" rel="stylesheet">
<style>
  :root {
    --backdrop: #e6e6e4;
    --yellow: #f3dc5a;
    --ink: #222222;
    --white: #f8f8f7;
    --alert-red: #e0352b;
    --xray-dark: #3a3a3a;
    --xray-mid: #7d7d7d;
  }
  * { box-sizing: border-box; margin: 0; padding: 0; }
  html, body {
    width: 1200px; height: 1200px; overflow: hidden;
    background: var(--backdrop);
    font-family: "Outfit", sans-serif;
  }
  .poster {
    position: absolute; left: 240px; top: 20px;
    width: 720px; height: 1160px;
    background: var(--yellow);
    padding: 20px 20px 26px;
  }
  .poster-inner {
    position: relative; width: 100%; height: 100%;
    background: var(--white);
  }
  .headline {
    position: absolute; top: 112px; left: 0; right: 0;
    text-align: center;
    font-weight: 800; font-size: 110px; line-height: 0.94;
    letter-spacing: -2px;
    color: var(--ink);
    text-shadow: 6px 5px 0 var(--yellow);
  }
  .comparison {
    position: absolute; top: 370px; left: 0; right: 0;
    height: 446px;
    display: flex; gap: 6px;
  }
  .xray { position: relative; flex: 1; }
  .xray-image {
    width: 100%; height: 100%;
    background: linear-gradient(180deg, var(--xray-mid) 0%, var(--xray-dark) 100%);
  }
  .xray-label {
    position: absolute; left: 50%; bottom: -24px;
    transform: translateX(-50%);
    width: 190px; height: 52px; border-radius: 12px;
    background: var(--yellow);
    display: flex; align-items: center; justify-content: center;
    font-weight: 700; font-size: 28px; color: var(--ink);
  }
  .warning {
    position: absolute; top: 893px; left: 60px;
    width: 562px; height: 168px;
    background: var(--yellow);
    border-radius: 14px;
    padding: 10px;
  }
  .warning-frame {
    width: 100%; height: 100%;
    border: 2.5px solid var(--ink);
    border-radius: 10px;
    display: flex; align-items: center;
  }
  .warning-icon { width: 124px; height: 110px; margin-left: 34px; flex: none; }
  .warning-divider {
    height: 108px; margin: 0 16px 0 20px;
    border-left: 4px dotted var(--ink);
  }
  .warning-text { color: var(--alert-red); white-space: nowrap; }
  .warning-kicker { font-weight: 700; font-size: 22px; line-height: 1.1; }
  .warning-title { font-weight: 700; font-size: 39px; line-height: 1.08; letter-spacing: -0.5px; }
</style>
</head>
<body>
  <main class="poster">
    <div class="poster-inner">
      <h1 class="headline">Do you feed<br>grain-free?</h1>

      <section class="comparison">
        <figure class="xray xray-normal">
          <div class="xray-image" role="img" aria-label="Chest x-ray of a dog with a normal sized heart"></div>
          <figcaption class="xray-label">Before</figcaption>
        </figure>
        <figure class="xray xray-enlarged">
          <div class="xray-image" role="img" aria-label="Chest x-ray of a dog with an enlarged heart after a grain-free diet"></div>
          <figcaption class="xray-label">After</figcaption>
        </figure>
      </section>

      <aside class="warning">
        <div class="warning-frame">
          <svg class="warning-icon" viewBox="0 0 124 110" aria-hidden="true">
            <polygon points="62,4 120,106 4,106" fill="#ffffff" stroke="#222222" stroke-width="3" stroke-linejoin="round"/>
            <rect x="55" y="38" width="14" height="40" rx="4" fill="#222222"/>
            <circle cx="62" cy="92" r="8" fill="#222222"/>
          </svg>
          <div class="warning-divider"></div>
          <div class="warning-text">
            <p class="warning-kicker">WARNING!</p>
            <p class="warning-title">Canine Dilated<br>Cardiomyopathy</p>
          </div>
        </div>
      </aside>
    </div>
  </main>
</body>
</html>
```